Corporate Business Cards

We need a new design for all of our business cards. They are boring and need some life.

Industry/Entity Type

Business

Requirements
Must have
• Corporate Logo of some type (See attached Pyramid)

Corporate Phrase "Accelerating Cashflow"

```html
<!DOCTYPE html>
<html lang="en">
<head>
<meta charset="utf-8">
<title>Ledgerway Partners – Business Card</title>
<link rel="stylesheet" href="https://fonts.googleapis.com/css2?family=Cinzel:wght@700&family=Open+Sans:wght@400;600;700&display=swap">
<style>
  :root {
    --page-bg: #d9d6d1;
    --card-bg: #eef0f2;
    --navy: #22256a;
    --navy-deep: #16184d;
    --brand: #2b2f78;
    --ink: #1d1d22;
    --muted: #6d6f74;
    --contact: #c9bb9f;
    --icon: #e4e4ea;
  }
  * { margin: 0; padding: 0; box-sizing: border-box; }
  html, body { width: 1200px; height: 970px; overflow: hidden; }
  body {
    background: var(--page-bg);
    font-family: "Open Sans", Arial, sans-serif;
    position: relative;
  }
  .card {
    position: absolute;
    left: 100px; top: 199px;
    width: 1000px; height: 572px;
    background: var(--card-bg);
    border: 1px solid #c9ccd2;
    overflow: hidden;
  }
  .card-art { position: absolute; inset: 0; }
  .brand-name {
    position: absolute; left: 46px; top: 60px;
    font-family: "Cinzel", Georgia, serif;
    font-weight: 700; font-size: 38px; letter-spacing: 0.5px;
    color: var(--brand); white-space: nowrap;
  }
  .tagline {
    position: absolute; left: 155px; top: 106px;
    font-size: 26px; color: var(--muted); white-space: nowrap;
  }
  .person { position: absolute; right: 88px; top: 108px; text-align: right; }
  .person-name { font-size: 35px; font-weight: 600; color: var(--ink); line-height: 1.2; }
  .person-title { font-size: 19px; font-weight: 700; color: var(--muted); }
  .address {
    position: absolute; left: 54px; top: 342px;
    font-size: 21px; line-height: 29px; color: #2a2b30; font-style: normal;
  }
  .contacts {
    position: absolute; right: 72px; top: 406px;
    list-style: none; text-align: right;
  }
  .contacts li {
    display: flex; align-items: center; justify-content: flex-end;
    gap: 18px; height: 33.5px;
    font-size: 20px; color: var(--contact); white-space: nowrap;
  }
  .contacts svg { width: 24px; height: 24px; flex: none; }
</style>
</head>
<body>
  <section class="card">
    <svg class="card-art" viewBox="0 0 1000 572" width="1000" height="572" aria-hidden="true">
      <defs>
        <linearGradient id="navyFill" x1="0" y1="1" x2="1" y2="0">
          <stop offset="0" stop-color="#2a2d78"/>
          <stop offset="1" stop-color="#1b1d58"/>
        </linearGradient>
        <linearGradient id="lineFill" x1="0" y1="0" x2="1" y2="0">
          <stop offset="0" stop-color="#c3c5ca"/>
          <stop offset="1" stop-color="#8e9098"/>
        </linearGradient>
      </defs>
      <path d="M0 562 C 380 505, 760 345, 1000 142" fill="none" stroke="url(#lineFill)" stroke-width="7"/>
      <path d="M70 572 C 420 520, 770 385, 1000 183 L1000 572 Z" fill="url(#navyFill)"/>
    </svg>

    <div class="brand-name">LEDGERWAY PARTNERS</div>
    <div class="tagline">Keeping Revenue Moving</div>

    <div class="person">
      <div class="person-name">Daniel Hartwell</div>
      <div class="person-title">Managing Director</div>
    </div>

    <address class="address">
      Ledgerway Partners Corporation<br>
      4120 Birchwood Ln. Suite 300,<br>
      Plymouth, MN
    </address>

    <ul class="contacts">
      <li>612-555-0148
        <svg viewBox="0 0 24 24" aria-label="Office phone"><path d="M3 9c0-3 4-5 9-5s9 2 9 5l-1 2-4-1V8c-2-1-6-1-8 0v2l-4 1z" fill="#e4e4ea"/><path d="M6 13h12l2 7H4z" fill="#e4e4ea"/><circle cx="12" cy="16.5" r="2" fill="#22256a"/></svg>
      </li>
      <li>000-000-0000
        <svg viewBox="0 0 24 24" aria-label="Mobile phone"><rect x="7" y="2" width="10" height="20" rx="2" fill="none" stroke="#e4e4ea" stroke-width="1.8"/><circle cx="12" cy="18.5" r="1" fill="#e4e4ea"/></svg>
      </li>
      <li>dhartwell@ledgerwaymn.com
        <svg viewBox="0 0 24 24" aria-label="Email"><rect x="3" y="6" width="18" height="12" fill="#e4e4ea"/><path d="M3 6l9 7 9-7" fill="none" stroke="#22256a" stroke-width="1.4"/></svg>
      </li>
      <li>www.ledgerwaymn.com
        <svg viewBox="0 0 24 24" aria-label="Website"><g fill="none" stroke="#e4e4ea" stroke-width="1.5"><circle cx="12" cy="12" r="8"/><ellipse cx="12" cy="12" rx="3.5" ry="8"/><path d="M4 12h16M5.5 8h13M5.5 16h13"/></g></svg>
      </li>
    </ul>
  </section>
</body>
</html>
```